"Recently Leased" flyer for real estate agency

Looking to have a Recently Leased flyer designed. This will be delivered to apartments and houses closely situated to a property we have recently leased. The idea is to get the attention of owner/landlords in the area that may be considering leasing their property in the future and inform them of the great work we are doing locally. I would like the design to be a two sided flyer using the photoshop (PSD) template below (we would like to be able to edit this once complete should we need to update copy etc in the future). I would like the front page to look like our "for lease sign with the leased sticker on it and copy, I dont want it to look like a typical junk mail flyer.

Target Market(s)

Property owners and investors, male and female aged 28-70

Industry/Entity Type

Real Estate

Font styles to use
Sans Serif

Colors

Designer to choose colors to be used in the design.

Requirements
Must have
• Harbor Keystone Logo
• Contact information
• Copy supplied
Nice to have
• Slick, clean design,
Should not have
• too many colours or too busy a design.
• NO PROPERTY PHOTOS ON FRONT - I want this to be generic and not relate to a specific property image which might confuse people.

```html
<!DOCTYPE html>
<html lang="en">
<head>
<meta charset="utf-8">
<title>Harbor Keystone – Recently Leased Flyer</title>
<link rel="stylesheet" href="https://fonts.googleapis.com/css2?family=Lato:wght@400;700;900&display=swap">
<style>
  :root {
    --ink: #121619;
    --teal: #1e8c99;
    --teal-text: #1a7f8c;
    --paper: #ffffff;
    --body: #1f1f1f;
    --stage: #e9eaec;
    --panel-top: #1d2b37;
    --panel-bottom: #0c141c;
  }
  * { margin: 0; padding: 0; box-sizing: border-box; }
  html, body { width: 1200px; height: 1200px; overflow: hidden; }
  body {
    background: var(--stage);
    font-family: "Lato", sans-serif;
    position: relative;
  }
  .flyer {
    position: absolute;
    top: 88px;
    width: 471px;
    height: 1024px;
    background: var(--paper);
    overflow: hidden;
  }
  .flyer--front { left: 121px; }
  .flyer--back { left: 608px; }
  .flyer__shapes { position: absolute; inset: 0; }
  .brand {
    position: absolute;
    top: 70px;
    left: 0;
    width: 100%;
    text-align: center;
    color: var(--paper);
    font-weight: 700;
    font-size: 40px;
    letter-spacing: 0.5px;
  }
  .intro {
    position: absolute;
    left: 20px;
    right: 20px;
    text-align: center;
    color: var(--body);
    font-size: 16px;
    line-height: 20.4px;
  }
  .flyer--front .intro { top: 284px; }
  .flyer--back .intro { top: 284px; }
  .benefits {
    position: absolute;
    left: 54px;
    right: 30px;
    list-style: none;
    color: var(--paper);
    font-size: 16px;
    line-height: 20.4px;
  }
  .flyer--front .benefits { top: 462px; }
  .flyer--back .benefits { top: 410px; right: 22px; }
  .benefits li { position: relative; }
  .benefits li::before {
    content: "";
    position: absolute;
    left: -16px;
    top: 7px;
    width: 7px;
    height: 7px;
    border-radius: 50%;
    background: var(--paper);
  }
  .call-to-action {
    position: absolute;
    top: 746px;
    left: 26px;
    right: 26px;
    text-align: center;
    color: var(--teal-text);
    font-size: 16px;
    line-height: 20.4px;
  }
  .agent-card {
    position: absolute;
    top: 853px;
    left: 103px;
    width: 266px;
    height: 55px;
    background: var(--ink);
    border: 2px solid var(--teal);
    border-radius: 9px;
    text-align: center;
    color: var(--teal);
  }
  .agent-card__name {
    display: block;
    font-weight: 700;
    font-size: 32px;
    line-height: 32px;
    margin-top: 4px;
  }
  .agent-card__agency {
    display: block;
    font-weight: 700;
    font-size: 11.5px;
    line-height: 13px;
  }
  .contact {
    position: absolute;
    top: 936px;
    left: 0;
    width: 100%;
    text-align: center;
    color: var(--paper);
    font-weight: 700;
    font-size: 16px;
    line-height: 20.4px;
  }
</style>
</head>
<body>

<article class="flyer flyer--front">
  <svg class="flyer__shapes" viewBox="0 0 471 1024" width="471" height="1024" aria-hidden="true">
    <defs>
      <linearGradient id="panelFront" x1="0" y1="0" x2="0" y2="1">
        <stop offset="0" stop-color="var(--panel-top)"/>
        <stop offset="1" stop-color="var(--panel-bottom)"/>
      </linearGradient>
    </defs>
    <path d="M0 0 H471 V224 Q230 270 0 220 Z" fill="var(--teal)"/>
    <path d="M0 0 H471 V212 Q230 256 0 200 Z" fill="var(--ink)"/>
    <path d="M0 900 Q260 850 471 902 V1024 H0 Z" fill="var(--teal)"/>
    <path d="M0 912 Q260 880 471 928 V1024 H0 Z" fill="var(--ink)"/>
  </svg>
  <svg class="flyer__shapes" viewBox="0 0 471 1024" width="471" height="1024" role="img" aria-label="Dim evening photo of a modern apartment courtyard">
    <path d="M0 424 L471 444 V730 L0 708 Z" fill="url(#panelFront)"/>
  </svg>

  <h1 class="brand">HARBOR KEYSTONE</h1>

  <p class="intro">We recently leased a property in your building or street. Attracting a great reliable tenant and fantastic return for the owner.<br>We received a high number of enquires and applications for this property and have a database of screened and qualified tenants looking to lease in your area.</p>

  <ul class="benefits">
    <li>On average we lease properties 2 weeks faster than the Eastern Shores average</li>
    <li>Strong database of tenants actively looking in the area</li>
    <li>All we do is lease property, no sales – so tenanting and managing your property is our priority</li>
    <li>90 day money back guarantee on our level of service</li>
    <li>Highly competitive, simple all-inclusive pricing.</li>
    <li>Experience the difference of a property management specialist</li>
  </ul>

  <p class="call-to-action">Contact Liam to get your free rental appraisal or transfer your existing investment to an agency that will give it the attention it deserves and maxamise your return.</p>

  <div class="agent-card">
    <span class="agent-card__name">LIAM CARTER</span>
    <span class="agent-card__agency">HARBOR KEYSTONE AGENCY</span>
  </div>

  <p class="contact">Level 2, 18 Marlow St, Fairhaven NSW 2199<br>www.harborkeystone.com.au<br>0400 555 218 | liam@harborkeystone.com.au</p>
</article>

<article class="flyer flyer--back">
  <svg class="flyer__shapes" viewBox="0 0 471 1024" width="471" height="1024" aria-hidden="true">
    <defs>
      <linearGradient id="panelBack" x1="0" y1="0" x2="0" y2="1">
        <stop offset="0" stop-color="var(--panel-top)"/>
        <stop offset="1" stop-color="var(--panel-bottom)"/>
      </linearGradient>
    </defs>
    <path d="M0 0 H471 V224 Q230 270 0 220 Z" fill="var(--teal)"/>
    <path d="M0 0 H471 V212 Q230 256 0 200 Z" fill="var(--ink)"/>
    <path d="M0 900 Q260 850 471 902 V1024 H0 Z" fill="var(--teal)"/>
    <path d="M0 912 Q260 880 471 928 V1024 H0 Z" fill="var(--ink)"/>
  </svg>
  <svg class="flyer__shapes" viewBox="0 0 471 1024" width="471" height="1024" role="img" aria-label="Dim evening photo of a modern apartment courtyard">
    <path d="M0 378 L471 398 V730 L0 708 Z" fill="url(#panelBack)"/>
  </svg>

  <h1 class="brand">HARBOR KEYSTONE</h1>

  <p class="intro">The fundamental idea behind Harbor Keystone Agency was to give landlords a simple and confidence inspiring experience. We achieve this through:</p>

  <ul class="benefits">
    <li>Unique marketing that goes beyond the standard listing sites and has seen our average days-on-market at 5.9days for 2018.</li>
    <li>A simple, yet competitive fee structure.</li>
    <li>Excellent customer service through an experi­enced professional property manager.</li>
    <li>Sound advice and communication through out the leasing and management process.</li>
    <li>A simple yet powerful landlord portal which enables owners to view media rich inspection reports, financial reports and maintenance prog­ress at anytime.</li>
    <li>We then back our service promise with a 90day money back guarantee.</li>
  </ul>

  <p class="call-to-action">If you have been considering leasing your property, purchasing a local investment or aren’t happy with your current managing agency, please don’t hesitate to contact your local rental specialist for more information:</p>

  <div class="agent-card">
    <span class="agent-card__name">LIAM CARTER</span>
    <span class="agent-card__agency">HARBOR KEYSTONE AGENCY</span>
  </div>

  <p class="contact">Level 2, 18 Marlow St, Fairhaven NSW 2199<br>www.harborkeystone.com.au<br>0400 555 218 | liam@harborkeystone.com.au</p>
</article>

</body>
</html>
```